Business Card Design for LeafCrest (Farming Devices)

We need Business Cards for our new Company based in Switzerland called "LeafCrest" We develop innovativ products for indoor and outdoor Farming for household and components for vertical farming. Our initial BloomNest gives people the possibility to grow their own food at home all year round. The design should communicate freshness, innovation, health.

```html
<!DOCTYPE html>
<html lang="en">
<head>
<meta charset="utf-8">
<title>LeafCrest Business Card</title>
<link href="https://fonts.googleapis.com/css2?family=Open+Sans:wght@400;600;700&display=swap" rel="stylesheet">
<style>
  :root {
    --stage: #2a2b2d;
    --brand-blue: #1a73c4;
    --deep-blue: #1768b3;
    --leaf-green: #6ab42d;
    --paper: #ffffff;
    --ink-white: #ffffff;
  }
  * { margin: 0; padding: 0; box-sizing: border-box; }
  html, body { width: 1200px; height: 874px; overflow: hidden; }
  body {
    background: var(--stage);
    font-family: "Open Sans", Arial, sans-serif;
    position: relative;
  }
  .card {
    position: absolute;
    left: 320px;
    width: 560px;
    height: 320px;
    border-radius: 18px;
    overflow: hidden;
  }
  .card-front {
    top: 72px;
    background: var(--brand-blue);
    display: flex;
    align-items: center;
    justify-content: center;
  }
  .front-name {
    color: var(--leaf-green);
    font-weight: 600;
    font-size: 66px;
    letter-spacing: -1px;
  }
  .card-back {
    top: 482px;
    background: var(--paper);
  }
  .back-panel {
    position: absolute;
    inset: 0;
    width: 100%;
    height: 100%;
  }
  .contact-list {
    position: absolute;
    left: 30px;
    top: 118px;
    list-style: none;
    color: var(--ink-white);
    font-size: 13px;
    line-height: 19px;
  }
  .contact-list li {
    display: flex;
    align-items: flex-start;
    gap: 8px;
  }
  .contact-list svg {
    width: 11px;
    height: 11px;
    margin-top: 4px;
    flex: none;
    fill: var(--leaf-green);
  }
  .contact-list .spacer { width: 11px; flex: none; }
  .identity {
    position: absolute;
    right: 40px;
    top: 112px;
    text-align: center;
  }
  .back-name {
    color: var(--leaf-green);
    font-weight: 600;
    font-size: 38px;
    letter-spacing: -0.5px;
    line-height: 1.1;
  }
  .person-name {
    color: var(--deep-blue);
    font-weight: 700;
    font-size: 19px;
    margin-top: 2px;
  }
  .person-title {
    color: var(--leaf-green);
    font-size: 12px;
  }
</style>
</head>
<body>
  <section class="card card-front">
    <div class="front-name">LeafCrest</div>
  </section>

  <section class="card card-back">
    <svg class="back-panel" viewBox="0 0 560 320" preserveAspectRatio="none">
      <path d="M0 0 H70 C250 20 320 170 230 320 H0 Z" fill="var(--brand-blue)"/>
      <path d="M70 0 C250 20 320 170 230 320" fill="none" stroke="var(--leaf-green)" stroke-width="4"/>
    </svg>

    <ul class="contact-list">
      <li><svg viewBox="0 0 12 12"><path d="M6 0a4 4 0 0 0-4 4c0 3 4 8 4 8s4-5 4-8a4 4 0 0 0-4-4zm0 5.5a1.5 1.5 0 1 1 0-3 1.5 1.5 0 0 1 0 3z"/></svg><span>2140 Alder Court</span></li>
      <li><span class="spacer"></span><span>Lucerne, Switzerland 6003</span></li>
      <li><svg viewBox="0 0 12 12"><path d="M2.5 0.5l2 2.5-1 1.5c.8 1.6 2 2.8 3.5 3.5l1.5-1 2.5 2-1.2 2C5.5 11 1 6.5 0.5 1.7z"/></svg><span>041-482-7310</span></li>
      <li><svg viewBox="0 0 12 12"><path d="M3 0h6v12H3zM4 1.5v8h4v-8z"/></svg><span>041-596-2248</span></li>
      <li><svg viewBox="0 0 12 12"><path d="M3 0h6v3H3zM0 4h12v5H9.5v3h-7V9H0zM3.5 8v3h5V8z"/></svg><span>041-673-9105</span></li>
      <li><svg viewBox="0 0 12 12"><path d="M0 2h12v8H0zM1 3l5 3.5L11 3z"/></svg><span>hartmann@leafcrest.com</span></li>
      <li><svg viewBox="0 0 12 12"><circle cx="6" cy="6" r="6"/></svg><span>www.leafcrest.com</span></li>
    </ul>

    <div class="identity">
      <div class="back-name">LeafCrest</div>
      <div class="person-name">Daniel Hartmann</div>
      <div class="person-title">President</div>
    </div>
  </section>
</body>
</html>
```